Trifold pamphlet for accommodation, cafe and tour business

I require a design that really stands out!
Light and bright but not garish.

See the pamphlet I have created.
This is the LAYOUT, LOGO, PHOTOS AND COPY I must have!

I require, back ground colours, images and designs to sit behind and around photos and copy.
Copy to be laid out correctly, photos laid out correctly, headings laid out correctly .
The pamphlet must flow and be captivating and want people to come visit!

I will need to provide you with high resolution photos.
Finally, I want the map provided to have our business located on it plus 2 other names.

Words that describe the business are:
Professional
Eco
Green.
Rainforest.
Birds.
Wildlife.
Adventure
Nature
Family owned and run
Family friendly.
Relaxing and beautiful.

Please check out our websites
www.tallowbrook.com.au
www.ridgeleyjourneys.com
www.facebook.com/tallowbrook
www.facebook.com/tallowbrookcafe
www.facebook.com/ridgeleyjourneys.com

I will need to provide high resolution photos.
Finally, I want the map provided to have our business located on it plus 2 other names

Thank you
Dale
dale@tallowbrook.com.au

Target Market(s)

Travellers, birdwatchers, adventurers, nature enthusiasts, family, friendly

Industry/Entity Type

Tourism

Font styles to use
Sans Serif

Colors
9bcb3c
add136
85cae6
ec1f27
fbed24

Requirements
Must have
• I require a design that really stands out!

```html
<!DOCTYPE html>
<html lang="en">
<head>
<meta charset="utf-8">
<title>Tallowbrook Trifold – Inside Spread</title>
<link href="https://fonts.googleapis.com/css2?family=Montserrat:wght@400;500;600;700&display=swap" rel="stylesheet">
<style>
  :root {
    --green: #6aaf3a;
    --green-light: #9bcb3c;
    --red: #b5404b;
    --white: #ffffff;
    --paper: #f2f2f2;
    --ink: #333333;
    --label: #3a3d3c;
    --stage: #4a4a4a;
  }
  * { box-sizing: border-box; margin: 0; padding: 0; }
  html, body { width: 1200px; height: 800px; overflow: hidden; }
  body { background: var(--stage); font-family: "Montserrat", sans-serif; color: var(--ink); }

  .spread {
    position: absolute; left: 60px; top: 20px;
    width: 1080px; height: 760px;
    display: flex;
    border-bottom: 4px solid var(--red);
  }
  .panel { position: relative; width: 360px; height: 100%; overflow: hidden; }
  .panel + .panel { border-left: 1px solid #dcdcdc; }
  .panel-intro { background: var(--white); }
  .panel-rooms, .panel-vip { background: var(--paper); }
  .panel svg.shape { position: absolute; left: 0; width: 100%; }

  .heading {
    position: absolute; left: 28px;
    font-weight: 600; text-transform: uppercase; letter-spacing: 1px;
    color: var(--white); font-size: 24px; line-height: 1.1;
  }

  /* Intro panel */
  .intro-copy { position: absolute; left: 28px; right: 26px; top: 100px; font-size: 12px; line-height: 1.4; }
  .intro-copy p + p { margin-top: 12px; }
  .area-tab {
    position: absolute; left: 40px; top: 392px; width: 230px; height: 40px;
    background: var(--red); color: var(--white);
    font-weight: 600; font-size: 23px; letter-spacing: 1px; text-transform: uppercase;
    padding: 6px 0 0 22px;
    clip-path: polygon(0 0, 88% 0, 100% 100%, 0 100%);
  }
  .area-list {
    position: absolute; left: 40px; right: 20px; top: 450px;
    list-style: none; color: var(--white); font-size: 11px; line-height: 1.35;
    border-left: 1px solid rgba(255,255,255,.7); padding-left: 0;
  }
  .area-list li { position: relative; padding-left: 24px; margin-bottom: 8px; }
  .area-list li:last-child { margin-bottom: 0; }
  .area-list li svg { position: absolute; left: -8px; top: 1px; }
  .area-list strong { font-weight: 700; }
  .area-list .soft { opacity: .85; }

  /* Photos */
  .photo { position: absolute; left: 30px; width: 300px; }
  .photo .fill { position: absolute; inset: 0; }
  .photo .frame { position: absolute; inset: 10px; border: 1px solid var(--red); opacity: .7; }
  .photo .label {
    position: absolute; left: 50%; top: 50%; transform: translate(-50%, -50%);
    background: var(--label); color: var(--white);
    font-weight: 500; font-size: 15px; letter-spacing: 1px; text-transform: uppercase;
    padding: 8px 22px; white-space: nowrap; text-align: center;
  }
  .photo .label.mixed { text-transform: none; font-size: 16px; line-height: 1.2; }
  .room-ensuite { top: 100px; height: 190px; }
  .room-ensuite .fill { background: linear-gradient(135deg, #d8d2c4, #a99a82 60%, #6e6a5e); }
  .room-single { top: 315px; height: 190px; }
  .room-single .fill { background: linear-gradient(135deg, #efe9dc, #c7b8a0 55%, #6b6560); }
  .beach-house { top: 530px; height: 200px; }
  .beach-house .fill { background: linear-gradient(180deg, #7cc2e4, #3fb2c4 45%, #4d8f3a 75%, #2f6b2c); }

  /* VIP panel */
  .vip-intro { position: absolute; left: 28px; right: 24px; top: 120px; font-size: 11.5px; line-height: 1.4; }
  .vip-house { top: 190px; height: 270px; }
  .vip-house .fill { background: linear-gradient(160deg, #e9eaec, #9fa3a6 55%, #55595c); }
  .cafe-heading {
    position: absolute; left: 28px; top: 488px;
    font-weight: 600; font-size: 24px; letter-spacing: 1px; text-transform: uppercase;
  }
  .cafe-heading .brand { color: var(--red); }
  .cafe-heading .word { color: var(--green); }
  .cafe-copy { position: absolute; left: 28px; right: 24px; top: 522px; font-size: 11.5px; line-height: 1.4; }
  .cafe-food { top: 572px; height: 165px; }
  .cafe-food .fill { background: linear-gradient(135deg, #d9cbb7, #a8703f 50%, #5a2a2a); }
</style>
</head>
<body>
<main class="spread">

  <section class="panel panel-intro">
    <svg class="shape" style="top:0" height="100" viewBox="0 0 360 100" preserveAspectRatio="none" aria-hidden="true">
      <path d="M0 0H360V78Q180 60 0 100Z" fill="var(--green)"/>
    </svg>
    <h2 class="heading" style="top:46px">The Tallowbrook</h2>
    <div class="intro-copy">
      <p>We are a friendly and family run accommodation, cafe and tour business. Sitting on 250 acres of rainforest bordered by the incredible Iron Range National Park</p>
      <p>The Tallowbrook has Ensuite rooms, family rooms, single rooms, and private VIP accomodation. Our beach house at Portland Roads is also available.</p>
      <p>All have air conditioning and verandahs surrounded by beautiful gardens and scenery.</p>
      <p>We also have a Cafe, Guest kitchen, free WIFI, BBQ area, fire pit, plenty of parking, walking tracks and plenty of info on how to get to the best spots.</p>
    </div>
    <svg class="shape" style="top:412px" height="348" viewBox="0 0 360 348" preserveAspectRatio="none" aria-hidden="true">
      <path d="M0 20Q180 -10 360 14V348H0Z" fill="var(--green)"/>
    </svg>
    <div class="area-tab">The Area</div>
    <ul class="area-list">
      <li><svg width="16" height="16" viewBox="0 0 16 16"><circle cx="8" cy="8" r="6.5" fill="var(--green)" stroke="#fff"/><path d="M5 8.2l2 2 4-4" stroke="#fff" fill="none" stroke-width="1.3"/></svg><span class="soft">Come visit</span> <strong>Kutini Payamu (Iron range) N.P</strong> <span class="soft">World renowned for incredible rainforest, famous birdwatching, wildlife and rich in biodiversity.</span></li>
      <li><svg width="16" height="16" viewBox="0 0 16 16"><circle cx="8" cy="8" r="6.5" fill="var(--green)" stroke="#fff"/><path d="M5 8.2l2 2 4-4" stroke="#fff" fill="none" stroke-width="1.3"/></svg><strong>Great Barrier Reef</strong> <span class="soft">- it speaks for itself!</span></li>
      <li><svg width="16" height="16" viewBox="0 0 16 16"><circle cx="8" cy="8" r="6.5" fill="var(--green)" stroke="#fff"/><path d="M5 8.2l2 2 4-4" stroke="#fff" fill="none" stroke-width="1.3"/></svg><strong>Portland Roads</strong> <span class="soft">- a tiny but beautiful and historical beach community</span></li>
      <li><svg width="16" height="16" viewBox="0 0 16 16"><circle cx="8" cy="8" r="6.5" fill="var(--green)" stroke="#fff"/><path d="M5 8.2l2 2 4-4" stroke="#fff" fill="none" stroke-width="1.3"/></svg><strong>Chili beach N.P</strong> <span class="soft">- white sandy beach covered in palm trees over looking the Coral Sea. As good as it gets</span></li>
      <li><svg width="16" height="16" viewBox="0 0 16 16"><circle cx="8" cy="8" r="6.5" fill="var(--green)" stroke="#fff"/><path d="M5 8.2l2 2 4-4" stroke="#fff" fill="none" stroke-width="1.3"/></svg><strong>Wattle Creek Arts Centre</strong> <span class="soft">- World famous for our local indigenous artists.</span></li>
      <li><svg width="16" height="16" viewBox="0 0 16 16"><circle cx="8" cy="8" r="6.5" fill="var(--green)" stroke="#fff"/><path d="M5 8.2l2 2 4-4" stroke="#fff" fill="none" stroke-width="1.3"/></svg><strong>Wattle Creek Aboriginal Community -</strong> <span class="soft">Friendly and helpful indigenous community with General store, Health Care clinic, police station, Post office, bank ATM, mechanical workshop, fuel, Airport.</span></li>
    </ul>
  </section>

  <section class="panel panel-rooms">
    <svg class="shape" style="top:0" height="90" viewBox="0 0 360 90" preserveAspectRatio="none" aria-hidden="true">
      <path d="M0 0H360V56Q180 40 0 78Z" fill="var(--green)"/>
    </svg>
    <h2 class="heading" style="top:30px">Tallowbrook Rooms</h2>
    <figure class="photo room-ensuite">
      <div class="fill" role="img" aria-label="Photo of an ensuite room with bed, desk and chair"></div>
      <div class="frame"></div>
      <figcaption class="label">Ensuited</figcaption>
    </figure>
    <figure class="photo room-single">
      <div class="fill" role="img" aria-label="Photo of a bright single room with a rug and armchair"></div>
      <div class="frame"></div>
      <figcaption class="label">Single Room</figcaption>
    </figure>
    <figure class="photo beach-house">
      <div class="fill" role="img" aria-label="Photo of a turquoise bay framed by palm trees at Portland Roads"></div>
      <div class="frame"></div>
      <figcaption class="label mixed">Our Beach house -<br>Portland Roads</figcaption>
    </figure>
  </section>

  <section class="panel panel-vip">
    <svg class="shape" style="top:0" height="120" viewBox="0 0 360 120" preserveAspectRatio="none" aria-hidden="true">
      <path d="M0 0H360V92Q180 80 0 112Z" fill="var(--green)"/>
    </svg>
    <h2 class="heading" style="top:34px">Iron Range<br>VIP Accommodation</h2>
    <p class="vip-intro">Stay in our newly built 2 bedroom houses that are private, modern and have panoramic views over the rainforest and out towards the Iron Range.</p>
    <figure class="photo vip-house">
      <div class="fill" role="img" aria-label="Photo of a modern open-plan living space with kitchen and large windows"></div>
      <div class="frame"></div>
    </figure>
    <h2 class="cafe-heading"><span class="brand">Tallowbrook</span> <span class="word">Cafe</span></h2>
    <p class="cafe-copy">Enjoy a good barista coffee, delicious home made pizzas, burgers, cakes and snacks!</p>
    <figure class="photo cafe-food">
      <div class="fill" role="img" aria-label="Photo of a burger, a coffee and a slice of red velvet cake"></div>
      <div class="frame"></div>
    </figure>
  </section>

</main>
</body>
</html>
```